EAT DIRT! Packaging redesign for Zingopods Energy Bites

We are redesigning our packaging for Zingopods Energy Bites, a healthy snack for people who want to build a better world. This brand is about action, health, and authenticity
Right now we need mockups of 4 different packaging aesthetics to survey customers about. We will then pick a winner and create a final design.
The four aesthetics are:
1. Hipster-ish
2. Vaporwave/retro
3. Kid-friendly
4. Hippy Snacks
We were working with a graphic designer who unfortunately passed away. We're hoping you can pick up where he left off. He completed a mockup for the hipster aesthetic, and a concept sketch for kid friendly.
The brand archetype for zingopods is Jester/Outlaw. Zingopod enthusiasts question mainstream assumptions about the world. We want to create better systems of spiritual actualization, and have as much fun as possible doing it.
Important points for the packaging:
-Drink water, breathe air, eat dirt
-Dates, Papaya, coconut
-Simple whole food ingredients
-Soft & chewy
-Made by humans
These will be custom printed, so don't feel constrained to the brown kraft paper. it can be any color we imagine. It important to have the window on the pouch, though.
A good job on this project WILL lead to more design work for you.

```html
<!DOCTYPE html>
<html lang="en">
<head>
<meta charset="utf-8">
<title>Zingopods Energy Bites – Pouch Front</title>
<link rel="stylesheet" href="https://fonts.googleapis.com/css2?family=Jost:wght@500;600;700&family=Josefin+Sans:wght@600&display=swap">
<style>
  :root {
    --backdrop: #ededed;
    --pouch-gold: #e2aa3c;
    --pouch-gold-light: #efc159;
    --pouch-gold-deep: #c98b22;
    --mud-brown: #8a5f1c;
    --label-black: #2f2f2f;
    --ink-white: #ffffff;
    --window-white: #ffffff;
    --window-text: #a9a9a9;
    --hang-hole: #e4e4e4;
    --silhouette: #3b3128;
  }

  * { box-sizing: border-box; margin: 0; padding: 0; }

  html, body {
    width: 1200px;
    height: 1200px;
    overflow: hidden;
    background: var(--backdrop);
  }

  .canvas {
    position: relative;
    width: 1200px;
    height: 1200px;
    font-family: "Jost", sans-serif;
  }

  .pouch-front {
    position: absolute;
    left: 278px;
    top: 55px;
    width: 650px;
    height: 1095px;
    background: linear-gradient(90deg, var(--pouch-gold-deep) 0%, var(--pouch-gold-light) 18%, var(--pouch-gold) 50%, var(--pouch-gold-light) 82%, var(--pouch-gold-deep) 100%);
    overflow: hidden;
  }

  .mud-texture {
    position: absolute;
    inset: 0;
    background:
      radial-gradient(ellipse 260px 420px at 55% 50%, rgba(138, 95, 28, 0.38), transparent 70%),
      radial-gradient(ellipse 180px 240px at 20% 85%, rgba(138, 95, 28, 0.3), transparent 70%),
      radial-gradient(ellipse 160px 200px at 85% 30%, rgba(138, 95, 28, 0.3), transparent 70%);
  }

  .brand-label {
    position: absolute;
    left: 177px;
    top: 2px;
    width: 303px;
    height: 328px;
    background: var(--label-black);
  }

  .hang-hole {
    position: absolute;
    left: 62px;
    top: 58px;
    width: 183px;
    height: 40px;
    border-radius: 20px;
    background: var(--hang-hole);
  }

  .brand-name {
    position: absolute;
    left: 0;
    right: 0;
    top: 185px;
    text-align: center;
    font-family: "Jost", sans-serif;
    font-weight: 700;
    font-size: 60px;
    line-height: 1;
    color: var(--ink-white);
  }

  .activity-scene {
    position: absolute;
    left: 122px;
    top: 335px;
    width: 450px;
    height: 115px;
    background: linear-gradient(180deg, rgba(59, 49, 40, 0.15), rgba(59, 49, 40, 0.55));
  }

  .ground-line {
    position: absolute;
    left: 102px;
    top: 452px;
    width: 470px;
    height: 2px;
    background: var(--silhouette);
  }

  .banner {
    position: absolute;
    left: 77px;
    top: 468px;
    width: 520px;
    height: 52px;
  }

  .banner svg { position: absolute; inset: 0; }

  .banner-text {
    position: absolute;
    inset: 0;
    display: flex;
    align-items: center;
    justify-content: center;
    padding-top: 4px;
    font-family: "Josefin Sans", sans-serif;
    font-weight: 600;
    font-size: 29px;
    letter-spacing: 3px;
    color: var(--ink-white);
  }

  .tagline {
    position: absolute;
    left: 0;
    right: 0;
    top: 537px;
    text-align: center;
    font-weight: 600;
    font-size: 26px;
    line-height: 28px;
    color: var(--ink-white);
    text-shadow: 1px 2px 3px rgba(0, 0, 0, 0.45);
  }

  .product-window {
    position: absolute;
    left: 45px;
    top: 635px;
    width: 540px;
    height: 305px;
    border-radius: 50%;
    background: var(--window-white);
    display: flex;
    align-items: center;
    justify-content: center;
  }

  .window-note {
    padding-top: 10px;
    font-weight: 500;
    font-size: 27px;
    letter-spacing: 1px;
    color: var(--window-text);
  }

  .flavour-list {
    position: absolute;
    left: 0;
    right: 0;
    top: 957px;
    text-align: center;
    font-weight: 600;
    font-size: 44px;
    line-height: 44px;
    color: var(--ink-white);
    text-shadow: 2px 3px 4px rgba(0, 0, 0, 0.5);
  }
</style>
</head>
<body>
<main class="canvas">
  <section class="pouch-front">
    <div class="mud-texture" role="img" aria-label="Muddy tyre tracks and footprints pattern in brown"></div>

    <header class="brand-label">
      <div class="hang-hole"></div>
      <h1 class="brand-name">Zingopods</h1>
    </header>

    <div class="activity-scene" role="img" aria-label="Dark silhouettes of a pine tree, a mountain biker, a hiker and a runner"></div>
    <div class="ground-line"></div>

    <div class="banner">
      <svg width="520" height="52" viewBox="0 0 520 52" aria-hidden="true">
        <polygon points="0,0 520,0 500,26 520,52 0,52 20,26" fill="#2f2f2f"/>
      </svg>
      <p class="banner-text">FOR ACTIVE PEOPLE</p>
    </div>

    <p class="tagline">DRINK WATER, BREATHE AIR<br>EAT DIRT</p>

    <div class="product-window">
      <span class="window-note">CLEAR AREA</span>
    </div>

    <p class="flavour-list">DATES • PAPAYA<br>COCONUT</p>
  </section>
</main>
</body>
</html>
```